DOUBLE SIDED BROCHURE NEEDED TO PROMOTE DOCTOR

I need a double sided DL size (99mm x 210mm) brochure, promoting a doctor seeing patients in a new area.

I want something professional. I have included the relevant information. I would also like the Dr's picture somwhere in the brochure, with a professional background. I wish to print these tomorrow, so i will pick a winner within 14 hours of posting this ad.

I have included an example of a brochures design that I recently saw, and its definietly a good starting point.

Medical

```html
<!DOCTYPE html>
<html lang="en">
<head>
<meta charset="utf-8">
<title>Referral Brochure – Dr. Karim Nassar</title>
<link href="https://fonts.googleapis.com/css2?family=Arimo:wght@400;700&display=swap" rel="stylesheet">
<style>
  :root{
    --bg:#e9ecef;
    --sky:#2fa8e6;
    --sky-light:#5cc4f3;
    --sky-pale:#9fdcf8;
    --navy:#0a6cc2;
    --deep:#075aa8;
    --white:#ffffff;
    --grey:#8a8d90;
    --heading:#27a3df;
  }
  *{box-sizing:border-box;margin:0;padding:0}
  html,body{width:1200px;height:724px;overflow:hidden}
  body{background:var(--bg);font-family:"Arimo",Arial,sans-serif;position:relative}
  .panel{position:absolute;top:32px;width:311px;height:660px;overflow:hidden;
    box-shadow:0 4px 14px rgba(0,0,0,.18)}
  .panel--front{left:250px;background:linear-gradient(180deg,var(--sky) 0%,var(--sky-light) 100%)}
  .panel--back{left:640px;background:var(--white)}

  /* front */
  .hero-photo{position:absolute;left:0;top:0;width:311px;height:270px;
    background:linear-gradient(180deg,#6fa9df 0%,#c9dff2 45%,#8d9299 75%,#4b5560 100%)}
  .hero-wave{position:absolute;left:0;top:215px;width:311px;height:100px}
  .letter{position:absolute;left:22px;top:318px;width:272px;color:var(--white)}
  .letter__greeting{font-size:25px;font-weight:700;margin-bottom:10px}
  .letter p{font-size:15.5px;line-height:1.22;margin-bottom:4px}
  .contact{position:absolute;left:22px;top:560px;color:var(--white)}
  .contact__title{font-size:17px;font-weight:700;margin-bottom:3px}
  .contact p{font-size:10.5px;line-height:1.35}
  .contact strong{font-weight:700}
  .fax-strip{position:absolute;left:0;bottom:0;width:311px;height:30px;background:var(--deep);
    color:var(--white);font-size:9.5px;font-weight:700;letter-spacing:1px;
    display:flex;align-items:center;justify-content:center}

  /* back */
  .intro{position:absolute;left:22px;top:46px;width:275px}
  .intro__heading{font-size:27px;font-weight:700;color:var(--heading);margin-bottom:6px}
  .intro__text{font-size:16px;line-height:1.5;color:var(--grey)}
  .back-wave{position:absolute;left:0;top:205px;width:311px;height:455px}
  .portrait{position:absolute;left:180px;top:228px;width:116px;height:116px;border-radius:50%;
    border:5px solid var(--navy);
    background:linear-gradient(180deg,#9cc7ec 0%,#d7e5f0 45%,#3a4450 100%)}
  .services{position:absolute;left:16px;top:330px;width:285px;color:var(--white);list-style:none}
  .services li{font-size:18.5px;line-height:1.2;padding-left:14px;position:relative;margin-bottom:3px}
  .services li::before{content:"";position:absolute;left:0;top:8px;width:6px;height:6px;border-radius:50%;background:var(--white)}
  .services li small{display:block;font-size:9.5px;margin-top:1px}
  .services .no-dot::before{display:none}
  .general-band{position:absolute;left:0;top:452px;width:250px;height:24px;background:var(--deep);
    color:var(--white);font-size:13px;display:flex;align-items:center;padding-left:16px}
  .services--general{top:484px}
  .services--general li{font-size:17.5px;line-height:1.2;margin-bottom:3px}
  .services--general li::before{top:7px}
</style>
</head>
<body>

<section class="panel panel--front" aria-label="Brochure front">
  <div class="hero-photo" role="img" aria-label="Photo of Dr. Karim Nassar standing in front of a modern hospital building under a cloudy blue sky"></div>
  <svg class="hero-wave" viewBox="0 0 311 100" preserveAspectRatio="none" aria-hidden="true">
    <path d="M0 30 Q150 85 311 25 L311 100 L0 100 Z" fill="#7fd0f6"/>
    <path d="M0 55 Q160 95 311 45 L311 100 L0 100 Z" fill="#ffffff"/>
    <path d="M0 72 Q160 108 311 62 L311 100 L0 100 Z" fill="#33aae7"/>
  </svg>

  <div class="letter">
    <h1 class="letter__greeting">Dear Doctors,</h1>
    <p>We are pleased to announce that Dr. Karim Nassar is now consulting in Harbourside, seeing public and private patients.</p>
    <p>Guaranteed appointment within two weeks, with patients having the option of surgery at Coastal Health Campus, Southgate General Hospital or Saint Clare Riverside.</p>
  </div>

  <div class="contact">
    <h2 class="contact__title">Contact</h2>
    <p>Harbourside Clinic:<br>42 Marina Parade, Harbourside WA 6000.<br>Phone: <strong>1300 000 111</strong></p>
  </div>

  <div class="fax-strip">Please send all referrals by fax to (08) 6000 2200.</div>
</section>

<section class="panel panel--back" aria-label="Brochure back">
  <div class="intro">
    <h2 class="intro__heading">Dr. Nassar is a</h2>
    <p class="intro__text">highly trained specialised surgeon, in all areas of Endocrine, Breast and General Surgery. Including;</p>
  </div>

  <svg class="back-wave" viewBox="0 0 311 455" preserveAspectRatio="none" aria-hidden="true">
    <defs>
      <linearGradient id="backBlue" x1="0" y1="0" x2="0" y2="1">
        <stop offset="0" stop-color="#2fa8e6"/>
        <stop offset="1" stop-color="#5cc4f3"/>
      </linearGradient>
    </defs>
    <path d="M0 25 Q120 -10 230 40 Q300 80 311 150 L311 455 L0 455 Z" fill="#0a6cc2"/>
    <path d="M0 40 Q120 8 225 55 Q290 90 296 160 L296 455 L0 455 Z" fill="url(#backBlue)"/>
  </svg>

  <div class="portrait" role="img" aria-label="Round portrait photo of Dr. Karim Nassar"></div>

  <ul class="services">
    <li>Thyroid Surgery</li>
    <li>Parathyroid Surgery<small>(including minimally invasive parathyroidectomy)</small></li>
    <li>Breast Cancer</li>
    <li class="no-dot">Benign breast lesions</li>
  </ul>

  <div class="general-band">All areas of general surgery, such as</div>

  <ul class="services services--general">
    <li>Gallbladder Surgery</li>
    <li>Hernia Surgery</li>
    <li>Haemorrhoids</li>
    <li>Carpal Tunnel</li>
    <li>Vasectomy etc etc...</li>
  </ul>
</section>

</body>
</html>
```